Kovalen Spinal Care and Performance

We need new business cards, something more modern, clean. On the back of the card maybe a quote. The Dr. likes, “The doctor of the future will give no medicine, but will interest his patient in the care of the human frame, in diet and in the cause and prevention of disease.” - Walter Brisby. We are open to other suggestions. We are a chiropractic office.

```html
<!DOCTYPE html>
<html lang="en">
<head>
<meta charset="utf-8">
<title>Kovalen Spinal Care and Performance – Business Card</title>
<link href="https://fonts.googleapis.com/css2?family=Raleway:wght@600;700&family=Roboto:wght@400;500&family=PT+Serif&display=swap" rel="stylesheet">
<style>
  :root {
    --bg: #1d1d1d;
    --card: #ffffff;
    --purple: #5e2a68;
    --green: #8cb833;
    --ink: #3a3a3a;
    --quote-ink: #333333;
  }
  * { margin: 0; padding: 0; box-sizing: border-box; }
  html, body { width: 1200px; height: 1200px; overflow: hidden; }
  body { background: var(--bg); position: relative; font-family: "Roboto", Arial, sans-serif; }

  .card {
    position: absolute;
    background: var(--card);
    border-radius: 14px;
    overflow: hidden;
  }
  .card--front { left: 118px; top: 558px; width: 588px; height: 336px; }
  .card--back { left: 746px; top: 306px; width: 336px; height: 588px; }

  .brand {
    position: absolute;
    display: flex;
    align-items: center;
    gap: 10px;
  }
  .brand__dot {
    width: 22px; height: 22px;
    border-radius: 50%;
    background: var(--green);
    flex: none;
  }
  .brand__name {
    font-family: "Raleway", Arial, sans-serif;
    font-weight: 700;
    color: var(--purple);
    line-height: 1.05;
    font-size: 30px;
    letter-spacing: 1px;
  }
  .brand__name small {
    display: block;
    font-size: 11px;
    letter-spacing: 0.5px;
    text-transform: uppercase;
  }
  .card--front .brand { left: 50px; top: 136px; }
  .card--back .brand { left: 40px; top: 410px; }
  .card--back .brand__name { font-size: 34px; }
  .card--back .brand__name small { font-size: 12.5px; }

  .divider {
    position: absolute;
    left: 294px; top: 104px;
    width: 3px; height: 126px;
    background: var(--green);
  }
  .person { position: absolute; left: 312px; top: 110px; }
  .person__name {
    font-family: "Raleway", Arial, sans-serif;
    font-weight: 700;
    font-size: 21px;
    color: var(--purple);
    line-height: 1.1;
  }
  .person__title {
    font-family: "Raleway", Arial, sans-serif;
    font-weight: 600;
    font-size: 18px;
    color: var(--green);
    line-height: 1.1;
  }
  .contact { list-style: none; margin-top: 22px; }
  .contact li {
    display: flex; align-items: center; gap: 6px;
    font-size: 16px; color: var(--ink);
    line-height: 20px;
  }
  .contact svg { width: 11px; height: 11px; fill: var(--ink); flex: none; }

  .address-band {
    position: absolute;
    left: 0; top: 278px;
    width: 100%; height: 28px;
    background: var(--purple);
    color: #fff;
    font-weight: 500;
    font-size: 15.5px;
    display: flex; align-items: center; justify-content: center; gap: 6px;
  }
  .address-band svg { width: 11px; height: 14px; fill: #fff; }

  .quote {
    position: absolute;
    left: 32px; top: 82px;
    width: 272px;
    font-family: "PT Serif", Georgia, serif;
    font-size: 17.5px;
    line-height: 30px;
    color: var(--quote-ink);
    text-align: justify;
    text-align-last: center;
  }
</style>
</head>
<body>

<section class="card card--front">
  <div class="brand">
    <span class="brand__dot"></span>
    <span class="brand__name">KOVALEN<small>Spinal Care and Performance</small></span>
  </div>
  <div class="divider"></div>
  <div class="person">
    <p class="person__name">DANA WHITLOCK</p>
    <p class="person__title">Director</p>
    <ul class="contact">
      <li><svg viewBox="0 0 24 24"><path d="M6.6 10.8a15 15 0 0 0 6.6 6.6l2.2-2.2a1 1 0 0 1 1-.25 11.4 11.4 0 0 0 3.6.57 1 1 0 0 1 1 1V20a1 1 0 0 1-1 1A17 17 0 0 1 3 4a1 1 0 0 1 1-1h3.5a1 1 0 0 1 1 1c0 1.25.2 2.45.57 3.57a1 1 0 0 1-.25 1z"/></svg>+1 416 555 0142</li>
      <li><svg viewBox="0 0 24 24"><path d="M2 5h20v14H2z M2 5l10 8 10-8" /></svg>dwhitlock@kovalen.com</li>
      <li><svg viewBox="0 0 24 24"><circle cx="12" cy="12" r="11"/></svg>www.kovalen.com</li>
    </ul>
  </div>
  <div class="address-band">
    <svg viewBox="0 0 24 30"><path d="M12 0a12 12 0 0 0-12 12c0 9 12 18 12 18s12-9 12-18A12 12 0 0 0 12 0zm0 17a5 5 0 1 1 0-10 5 5 0 0 1 0 10z"/></svg>
    248 Harbord Ave., Toronto ON Canada M5R 2K9
  </div>
</section>

<section class="card card--back">
  <p class="quote">“The doctor of the future will give no medicine, but will interest his patient in the care of the human frame, in diet and in the cause and prevention of disease.” - Walter Brisby.</p>
  <div class="brand">
    <span class="brand__dot"></span>
    <span class="brand__name">KOVALEN<small>Spinal Care and Performance</small></span>
  </div>
</section>

</body>
</html>
```